Sunmeadow Home Care Business Card

We are a home care company customizing in personal care services. Our personal care service is different because our mission is to provide the most effective care while enhancing quality of life. We strive to make everyday our client's best day. I would like a very classic and/or retro feel. I don't like clip art.

Target Market(s)

doctor's offices; potential clients

Industry/Entity Type

Business

Contact Information for Business Card

jdalton@sunmeadowhc.example(919) 480-15904000 Copper Finch Lane, Suite 101Raleigh, NC 27612www.SunmeadowHC.example

Requirements
Must have
• classic and/or retro feel. Very caring.
Should not have
• Clip art

```html
<!DOCTYPE html>
<html lang="en">
<head>
<meta charset="utf-8">
<title>Sunmeadow Home Care – Business Card</title>
<link rel="stylesheet" href="https://fonts.googleapis.com/css2?family=Open+Sans:wght@400;600;700&display=swap">
<style>
  :root {
    --backdrop: #3a393a;
    --sky: #0aa9e2;
    --sky-light: #1db4e8;
    --leaf: #8ccc4a;
    --leaf-light: #9fd65a;
    --paper: #ffffff;
    --ink-light: #ffffff;
  }
  * { box-sizing: border-box; margin: 0; padding: 0; }
  html, body {
    width: 1200px; height: 750px; overflow: hidden;
    background: var(--backdrop);
    font-family: "Open Sans", Arial, sans-serif;
  }
  .canvas { position: relative; width: 1200px; height: 750px; }
  .card {
    position: absolute; top: 225px;
    width: 525px; height: 300px;
    border-radius: 18px; overflow: hidden;
    box-shadow: 0 10px 24px rgba(0,0,0,.45);
  }
  /* Card back */
  .card-back {
    left: 50px;
    background: linear-gradient(135deg, var(--sky) 0%, var(--sky-light) 100%);
    display: flex; align-items: center; justify-content: center;
  }
  .card-back .wordmark {
    color: var(--ink-light); font-size: 30px; font-weight: 600;
  }
  /* Card front */
  .card-front { left: 625px; background: var(--paper); }
  .card-front .wordmark {
    position: absolute; left: 40px; top: 52px;
    color: var(--sky); font-size: 28px; font-weight: 600;
  }
  .person-panel {
    position: absolute; left: 0; top: 172px;
    width: 290px; height: 98px;
    background: var(--sky);
    border-radius: 0 14px 14px 0;
    color: var(--ink-light); text-align: right;
    padding: 14px 22px 0 0;
  }
  .person-name { font-size: 19px; font-weight: 700; line-height: 1.2; }
  .person-title { font-size: 13px; line-height: 1.3; }
  .person-web { font-size: 12.5px; margin-top: 12px; }
  .contact-panel {
    position: absolute; left: 303px; top: 108px;
    width: 222px; height: 110px;
    background: linear-gradient(135deg, var(--leaf) 0%, var(--leaf-light) 100%);
    border-radius: 14px 0 0 14px;
    color: var(--ink-light);
    padding: 14px 0 0 16px;
    font-size: 11px; line-height: 1.5;
  }
  .contact-address { margin-bottom: 6px; }
  .contact-line { display: flex; align-items: center; gap: 6px; }
  .contact-line svg { width: 12px; height: 12px; flex: none; }
</style>
</head>
<body>
<div class="canvas">
  <section class="card card-back">
    <span class="wordmark">Sunmeadow Home Care, Inc.</span>
  </section>

  <section class="card card-front">
    <span class="wordmark">Sunmeadow Home Care, Inc.</span>

    <div class="contact-panel">
      <p class="contact-address">Copper Finch Lane<br>Suite 101 Fairhollow, NC 27000</p>
      <p class="contact-line">
        <svg viewBox="0 0 12 12" aria-hidden="true"><path fill="#fff" d="M1 4.5C1 2.5 3 1.5 6 1.5s5 1 5 3l-2 .5-.5-1.3h-5L3 5ZM2.5 6h7l1 4.5h-9Z"/></svg>
        (555) 302-7741
      </p>
      <p class="contact-line">
        <svg viewBox="0 0 12 12" aria-hidden="true"><rect x="1" y="2.5" width="10" height="7" fill="#fff"/><path d="M1 2.5l5 4 5-4" fill="none" stroke="#8ccc4a" stroke-width="1"/></svg>
        jdalton@sunmeadowhc.example
      </p>
    </div>

    <div class="person-panel">
      <p class="person-name">Evan Harlow</p>
      <p class="person-title">Director</p>
      <p class="person-web">www.SunmeadowHC.example</p>
    </div>
  </section>
</div>
</body>
</html>
```